Professional Business Cards

We need a nice looking, profession and modern business card for our new company. Our logo is attatched

Target Market(s)

Young Professionals

Industry/Entity Type

Financial

Contact Information for Business Card

FRONT

Morvane Tally Pty Ltd
Level 22, Halden Court, 48 Wirrapool St
Sydney NSW 2000
ABN : 57 304 918 226

Derek Wallis - Chief Operations Officer
P : 02 7153 2819
M: 0418 395 207
derek@morvanetally,com

BACK

- Cryptocurrency Exchange Services
- Cryptocurrency Mining Operations
- Cryptocurrency Investment Fund Offering

Font styles to use
Sans Serif

Colors
0255a3
9d9d9d

```html
<!DOCTYPE html>
<html lang="en">
<head>
<meta charset="utf-8">
<title>Morvane Tally – Business Card</title>
<link rel="stylesheet" href="https://fonts.googleapis.com/css2?family=PT+Sans+Narrow:wght@400;700&display=swap">
<style>
  :root {
    --brand-blue: #0255a3;
    --brand-grey: #9d9d9d;
    --rule-grey: #7a7a7a;
    --ink: #1e1e1e;
    --ice: #a9d3f2;
    --paper: #ffffff;
    --frame: #8c8c8c;
  }
  * { margin: 0; padding: 0; box-sizing: border-box; }
  html, body {
    width: 875px;
    height: 1200px;
    overflow: hidden;
    background: var(--paper);
    font-family: "PT Sans Narrow", "Arial Narrow", sans-serif;
    color: var(--ink);
  }
  .canvas { position: relative; width: 875px; height: 1200px; }

  .card-front {
    position: absolute;
    left: 61px; top: 99px;
    width: 753px; height: 484px;
    border: 1.5px solid var(--frame);
    background: var(--paper);
  }
  .brand {
    position: absolute;
    left: 30px; top: 62px;
    display: flex; align-items: center; gap: 22px;
  }
  .brand-mark {
    width: 56px; height: 56px;
    background: var(--brand-blue);
  }
  .brand-name {
    font-size: 64px;
    font-weight: 700;
    color: var(--brand-blue);
    letter-spacing: 1px;
    line-height: 1;
  }
  .person {
    position: absolute;
    right: 48px; top: 258px;
    text-align: right;
  }
  .person-name { font-size: 24px; font-weight: 700; line-height: 1.1; }
  .person-title { font-size: 18px; margin-top: 8px; }

  .divider {
    position: absolute;
    left: 37px; top: 345px;
    width: 681px; height: 3px;
    display: flex;
  }
  .divider-blue { width: 438px; background: var(--brand-blue); }
  .divider-grey { flex: 1; background: var(--rule-grey); }

  .company-details, .contact-details {
    position: absolute;
    top: 362px;
    font-size: 18px;
    line-height: 25.5px;
  }
  .company-details { left: 37px; }
  .contact-details { left: 545px; }

  .card-back {
    position: absolute;
    left: 61px; top: 617px;
    width: 753px; height: 484px;
    background: var(--brand-blue);
    overflow: hidden;
  }
  .services {
    position: absolute;
    left: 325px; top: 30px;
    list-style: none;
    color: var(--paper);
    font-size: 26px;
    line-height: 41px;
  }
  .services li { display: flex; align-items: center; gap: 8px; }
  .bullet { width: 14px; height: 14px; flex: none; }
</style>
</head>
<body>
<div class="canvas">

  <section class="card-front">
    <div class="brand">
      <span class="brand-mark"></span>
      <span class="brand-name">MORVANE TALLY</span>
    </div>

    <div class="person">
      <p class="person-name">Derek Wallis</p>
      <p class="person-title">Chief Operations Officer</p>
    </div>

    <div class="divider">
      <span class="divider-blue"></span>
      <span class="divider-grey"></span>
    </div>

    <address class="company-details" style="font-style:normal">
      Morvane Tally Pty Ltd<br>
      Level 22, Halden Court, 48 Wirrapool St<br>
      Sydney NSW 2000<br>
      ABN : 57 304 918 226
    </address>

    <address class="contact-details" style="font-style:normal">
      P : 02 7153 2819<br>
      M: 0418 395 207<br>
      derek@morvanetally,com
    </address>
  </section>

  <section class="card-back">
    <ul class="services">
      <li><svg class="bullet" viewBox="0 0 14 14"><rect x="3" y="3" width="8" height="8" transform="rotate(45 7 7)" fill="var(--ice)"/></svg>Cryptocurrency Exchange Services</li>
      <li><svg class="bullet" viewBox="0 0 14 14"><rect x="3" y="3" width="8" height="8" transform="rotate(45 7 7)" fill="var(--ice)"/></svg>Cryptocurrency Mining Operations</li>
      <li><svg class="bullet" viewBox="0 0 14 14"><rect x="3" y="3" width="8" height="8" transform="rotate(45 7 7)" fill="var(--ice)"/></svg>Cryptocurrency Investment Fund Offering</li>
    </ul>
  </section>

</div>
</body>
</html>
```